Tovesca Website

I need a website for a startup company that provides GIS (Geographic Information Services) staffing and products for local cities. Current website is www.tovescagroup.com

```html
<!DOCTYPE html>
<html lang="en">
<head>
<meta charset="utf-8">
<title>Tovesca Group — We Make GIS Work For You</title>
<link rel="stylesheet" href="https://fonts.googleapis.com/css2?family=Michroma&family=Lexend:wght@300;400;500;600&display=swap">
<style>
:root{
  --ink:#0b0d12;
  --navy:#0a1220;
  --blue:#1a6fb3;
  --blue-bright:#2289d6;
  --grey:#f0f0f0;
  --field:#e9e9e9;
  --line:#d4d4d4;
  --text:#222;
  --muted:#555;
  --white:#fff;
}
*{box-sizing:border-box;margin:0;padding:0}
html,body{width:1200px;height:4511px;overflow:hidden}
body{position:relative;background:var(--white);font-family:"Lexend",sans-serif;color:var(--text)}
.display{font-family:"Michroma",sans-serif;text-transform:uppercase;letter-spacing:.02em;font-weight:400;-webkit-text-stroke:.045em currentColor}
.abs{position:absolute}
section,header,footer{position:absolute;left:0;width:1200px}

/* nav */
.site-header{top:0;height:75px;background:var(--ink)}
.brand{left:89px;top:25px;font-size:21px;color:var(--white)}
.menu{left:508px;top:32px;display:flex;gap:19px;font-family:"Michroma",sans-serif;font-size:10.5px;color:var(--white)}
.menu .active{color:var(--blue-bright)}
.contact-btn{right:0;top:0;width:198px;height:75px;background:var(--blue);color:var(--white);font-size:14px;display:flex;align-items:center;justify-content:center}

/* hero */
.hero{top:75px;height:675px;background:radial-gradient(ellipse at 75% 35%,#5c6470 0%,#2c333d 35%,#0c1522 75%)}
.hero-welcome{left:89px;top:395px;font-size:35px;color:var(--white)}
.hero-name{left:86px;top:432px;font-size:84px;color:var(--white);letter-spacing:.04em}
.hero-tag{left:89px;top:540px;font-size:28px;color:var(--white)}
.hero-badge{left:995px;top:431px;width:116px;height:116px;border-radius:50%;background:radial-gradient(circle,#1a6fb3 0 55%,#0a1220 57%)}

/* story */
.story{top:750px;height:512px;border-bottom:1px solid var(--line)}
.story-map{left:0;top:0;width:543px;height:512px;background:linear-gradient(135deg,#3d3a48,#57535f 55%,#3e84b8)}
.story-photo{left:1004px;top:0;width:196px;height:512px;background:linear-gradient(180deg,#8d9580,#5d6a46 45%,#4a4036)}
.story h2{left:599px;top:134px;font-size:35px}
.story h3{left:599px;top:186px;font-size:12.5px}
.story p{left:599px;top:207px;width:360px;font-size:14.5px;line-height:21px;color:var(--muted);font-weight:300}
.story-cta{left:614px;top:339px;width:76px;height:76px;border-radius:50%;background:var(--blue);display:flex;align-items:center;justify-content:center}

/* product */
.product{top:1262px;height:590px;border-bottom:1px solid #bbb}
.product h2{left:184px;top:146px;font-size:34px;line-height:42px}
.product .sub{left:184px;top:245px;width:420px;font-size:13.5px;text-transform:uppercase;line-height:19px}
.product-links{left:184px;top:293px;width:412px;list-style:none}
.product-links li{height:58px;display:flex;justify-content:space-between;align-items:center;font-family:"Michroma",sans-serif;font-size:13px;border-bottom:1px solid var(--line)}
.product-links li:last-child{border-bottom:none}
.product-links li.current{color:var(--blue)}
.product-photo{left:646px;top:89px;width:360px;height:415px;background:radial-gradient(circle at 50% 35%,#3e9be0,#1c4b7a 45%,#0f1d33);box-shadow:0 30px 40px rgba(0,0,0,.18)}

/* innovations */
.innovations{top:1852px;height:571px}
.innovations .kicker{left:0;width:1200px;top:34px;text-align:center;font-size:16px;text-transform:uppercase}
.innovations h2{left:0;width:1200px;top:58px;text-align:center;font-size:34px}
.tile{top:124px;height:447px;display:flex;align-items:flex-end;padding:0 0 38px 42px;color:var(--white);font-size:18px;line-height:22px}
.t1{left:0;width:301px;background:linear-gradient(180deg,#6e7c8c,#243245 60%,#0e1520)}
.t2{left:317px;width:301px;background:linear-gradient(180deg,#75858c,#3a5a3a 55%,#1a2418)}
.t3{left:634px;width:301px;background:linear-gradient(180deg,#3f6f9a,#1d3553 55%,#160f10)}
.t4{left:951px;width:249px;padding-left:26px;background:linear-gradient(180deg,#6f7a7c,#3b4a44 55%,#1d2426)}

/* services */
.services{top:2423px;height:669px;border-bottom:1px solid #bbb}
.services h2{left:0;width:1200px;top:82px;text-align:center;font-size:35px}
.svc{top:154px;width:330px;height:410px;background:var(--grey);padding:34px 28px}
.svc.featured{background:var(--blue);color:var(--white);box-shadow:0 30px 40px rgba(0,0,0,.22)}
.svc h3{margin-top:24px;font-size:30px;line-height:28px}
.svc h3 span{font-size:21px}
.svc ul{margin-top:18px;list-style:none;font-size:17px;line-height:30px;font-weight:300}
.svc ul li::before{content:"• "}
.svc.s1{left:88px}.svc.s2{left:434px}.svc.s3{left:780px}

/* latest */
.latest{top:3092px;height:482px;border-bottom:1px solid #bbb}
.latest .divider{left:773px;top:0;width:1px;height:482px;background:#bbb}
.news-photo{top:85px;width:293px;height:239px}
.n1{left:91px;background:linear-gradient(180deg,#c9d0d6,#7d868e 60%,#4c5054)}
.n2{left:399px;background:linear-gradient(180deg,#3a3230,#5a4a40 50%,#2a2624)}
.news-title{top:344px;width:293px;font-size:13.5px;line-height:21px}
.latest h2{left:809px;top:162px;font-size:33px;line-height:40px}
.arrows{left:809px;top:266px;display:flex;gap:8px}
.arrows span{width:32px;height:32px;display:flex;align-items:center;justify-content:center}

/* contact */
.contact{top:3574px;height:592px}
.contact .divider{left:527px;top:0;width:1px;height:382px;background:#bbb}
.contact-band{left:527px;top:382px;width:673px;height:210px;background:linear-gradient(135deg,#1665a8,#1d74bd)}
.contact .kicker{left:165px;top:205px;font-size:15px;color:var(--blue);font-weight:600;text-transform:uppercase}
.contact h2{left:165px;top:232px;font-size:36px;line-height:40px}
.contact p{left:165px;top:362px;width:315px;font-size:14.5px;line-height:21px;color:var(--muted);font-weight:300}
.form-card{left:592px;top:86px;width:419px;height:436px;background:var(--white);box-shadow:0 10px 30px rgba(0,0,0,.12);padding:40px 31px}
.form-card label{position:absolute;font-family:"Michroma",sans-serif;font-size:12.5px;text-transform:uppercase;-webkit-text-stroke:.04em currentColor}
.form-card label b{color:var(--blue);font-weight:400}
.field{position:absolute;background:var(--field);font-size:13px;color:#999;padding:0 15px;display:flex;align-items:center}
.robot{position:absolute;left:31px;top:349px;width:177px;height:50px;border:1px solid #ccc;background:#f9f9f9;display:flex;align-items:center;gap:12px;padding-left:14px;font-size:11px}
.robot i{width:20px;height:20px;border:2px solid #bbb;background:#fff}
.submit{position:absolute;left:265px;top:349px;width:123px;height:50px;background:var(--blue);color:var(--white);font-size:14px;display:flex;align-items:center;justify-content:center}

/* footer */
.site-footer{top:4166px;height:345px;background:var(--ink);color:var(--white)}
.site-footer h2{left:0;width:1200px;top:72px;text-align:center;font-size:45px}
.site-footer p{left:180px;width:840px;top:140px;text-align:center;font-size:15px;line-height:22px}
.social{left:501px;top:205px;display:flex;gap:9px}
.social span{width:42px;height:42px;border-radius:50%;background:#22252b}
.site-footer .rule{left:88px;top:284px;width:1024px;height:1px;background:#333}
.copyright{left:0;width:1200px;top:316px;text-align:center;font-size:12px}
.to-top{left:1127px;top:275px;width:56px;height:56px;border-radius:50%;background:var(--blue);border:3px solid #fff;display:flex;align-items:center;justify-content:center}
</style>
</head>
<body>

<header class="site-header">
  <div class="abs brand display">Tovesca Group</div>
  <nav class="abs menu"><span class="active">HOME</span><span>ABOUT</span><span>SERVICES</span><span>NEWS</span><span>INSIGHTS</span><span>SUPPORT</span></nav>
  <div class="abs contact-btn display">Contact Us</div>
</header>

<section class="hero">
  <div class="abs" style="inset:0" role="img" aria-label="Dark topographic map of a coastline with blue location markers"></div>
  <div class="abs hero-welcome display">Welcome to</div>
  <div class="abs hero-name display">Tovesca</div>
  <div class="abs hero-tag display">We make GIS work for you</div>
  <div class="abs hero-badge" role="img" aria-label="Round GIS emblem badge"></div>
</section>

<section class="story">
  <div class="abs story-map" role="img" aria-label="Night street map of a city crossed by a blue river"></div>
  <h2 class="abs display">Our Story</h2>
  <h3 class="abs display">Shaping Geographic Intelligence</h3>
  <p class="abs">We are an innovative team of geospatial experts with 25 years of experience in the field of GIS. We specialize in providing results-driven GIS solutions for local government and the private sector.</p>
  <div class="abs story-cta" role="img" aria-label="Read our story button">
    <svg width="36" height="30" viewBox="0 0 36 30"><path d="M4 15h26M20 5l11 10-11 10" stroke="#fff" stroke-width="6" fill="none" stroke-linecap="round" stroke-linejoin="round"/></svg>
  </div>
  <div class="abs story-photo" role="img" aria-label="Aerial view of green cliffs with a red location pin"></div>
</section>

<section class="product">
  <h2 class="abs display">Tovesca's<br>GeoVantor</h2>
  <div class="abs sub">The premier GIS mapping solution for innovative geospatial insights.</div>
  <ul class="abs product-links">
    <li>WHY TOVESCA GROUP?<svg width="22" height="22"><path d="M3 19L19 3M8 3h11v11" stroke="#111" stroke-width="2" fill="none"/></svg></li>
    <li class="current">GEOVANTOR, OVERVIEW<svg width="22" height="22"><path d="M3 19L19 3M8 3h11v11" stroke="#1a6fb3" stroke-width="2" fill="none"/></svg></li>
    <li>WHAT IS GIS?<svg width="22" height="22"><path d="M3 19L19 3M8 3h11v11" stroke="#111" stroke-width="2" fill="none"/></svg></li>
  </ul>
  <div class="abs product-photo" role="img" aria-label="Analyst seen from behind facing a glowing globe on a wall of screens"></div>
</section>

<section class="innovations">
  <div class="abs kicker">Cutting-edge innovations with Tovesca's</div>
  <h2 class="abs display">Geospatial Intelligence.</h2>
  <div class="abs tile t1 display" role="img" aria-label="City highway at sunset">Safer<br>Roads Data</div>
  <div class="abs tile t2 display" role="img" aria-label="Aerial view of green rooftops in a city">Smart City<br>Revolution</div>
  <div class="abs tile t3 display" role="img" aria-label="Engineer in front of a digital globe">Digital Twin<br>Preservation</div>
  <div class="abs tile t4 display" role="img" aria-label="Hand touching a map on a tablet">GIS Enterprise<br>Decisions</div>
</section>

<section class="services">
  <h2 class="abs display">Our Services</h2>
  <div class="abs svc s1">
    <svg width="80" height="80" viewBox="0 0 80 80" fill="none" stroke="#111" stroke-width="2.5"><circle cx="14" cy="12" r="6"/><circle cx="66" cy="12" r="6"/><rect x="30" y="4" width="20" height="14"/><path d="M4 76V36q0-10 10-10h6l10 14M76 76V36q0-10-10-10h-6l-10 14M20 76V44M60 76V44M28 46h24"/></svg>
    <h3 class="display">GIS<br><span>Consulting</span></h3>
    <ul><li>GIS projects</li><li>Staffing solutions</li><li>System architecture design</li><li>GIS analysis</li><li>Demographics</li><li>Map products</li></ul>
  </div>
  <div class="abs svc s2 featured">
    <svg width="80" height="80" viewBox="0 0 80 80" fill="none" stroke="#fff" stroke-width="2.5"><path d="M12 4h44l12 12v60H12z"/><rect x="18" y="12" width="34" height="14"/><text x="22" y="23" font-family="Michroma" font-size="9" fill="#fff" stroke="none">GIS</text><path d="M40 38l16 8-16 8-16-8zM24 52l16 8 16-8M24 58l16 8 16-8"/></svg>
    <h3 class="display">GIS<br><span>Applications</span></h3>
    <ul><li>TerraGIS Online</li><li>TerraGIS Enterprise</li><li>Dashboards</li><li>Layout Studio</li><li>Custom widgets</li><li>Custom JavaScript apps</li></ul>
  </div>
  <div class="abs svc s3">
    <svg width="80" height="80" viewBox="0 0 80 80" fill="none" stroke="#111" stroke-width="2.5"><path d="M4 14V4h10M66 4h10v10M4 66v10h10M76 66v10H66"/><path d="M40 44S28 30 28 22a12 12 0 0124 0c0 8-12 22-12 22z"/><circle cx="40" cy="22" r="4"/><path d="M24 40L10 54l30 12 30-12-14-14"/></svg>
    <h3 class="display">Spatial<br><span>Data Solutions</span></h3>
    <ul><li>Spatial data cleanup</li><li>GIS data model<br>&nbsp;&nbsp;design/review</li><li>Integrating with other<br>&nbsp;&nbsp;systems</li></ul>
  </div>
</section>

<section class="latest">
  <div class="abs news-photo n1" role="img" aria-label="Modern buildings beside a rail bridge"></div>
  <div class="abs news-photo n2" role="img" aria-label="Team meeting around a presentation screen"></div>
  <div class="abs news-title display" style="left:91px">Shaping tomorrow's infrastructure with Tovesca</div>
  <div class="abs news-title display" style="left:399px">Elevating enterprise solutions with Tovesca and Norvane</div>
  <div class="abs divider"></div>
  <h2 class="abs display">Latest<br>Innovations</h2>
  <div class="abs arrows">
    <span style="background:#111"><svg width="10" height="10"><path d="M7 1L3 5l4 4" stroke="#fff" stroke-width="2" fill="none"/></svg></span>
    <span style="background:var(--blue)"><svg width="10" height="10"><path d="M3 1l4 4-4 4" stroke="#fff" stroke-width="2" fill="none"/></svg></span>
  </div>
</section>

<section class="contact">
  <div class="abs divider"></div>
  <div class="abs contact-band" role="img" aria-label="Blue city street map pattern"></div>
  <div class="abs kicker">Get in touch with us!</div>
  <h2 class="abs display">Interested<br>in learning<br>more?</h2>
  <p class="abs">Reach out to us today, and let's discuss how we can assist you in achieving your geographic information goals.</p>
  <form class="abs form-card">
    <label style="left:31px;top:40px">First Name<b>*</b></label>
    <label style="left:214px;top:40px">Last Name<b>*</b></label>
    <div class="field" style="left:31px;top:62px;width:175px;height:42px">First Name</div>
    <div class="field" style="left:214px;top:62px;width:174px;height:42px">Last Name</div>
    <label style="left:31px;top:121px">Email<b>*</b></label>
    <label style="left:214px;top:121px">Company<b>*</b></label>
    <div class="field" style="left:31px;top:143px;width:175px;height:42px">Email address</div>
    <div class="field" style="left:214px;top:143px;width:174px;height:42px">Company</div>
    <label style="left:31px;top:200px">Message<b>*</b></label>
    <div class="field" style="left:31px;top:222px;width:357px;height:106px;align-items:flex-start;padding-top:16px">Type your questions</div>
    <div class="robot"><i></i>I'm not a robot</div>
    <div class="submit display">Submit</div>
  </form>
</section>

<footer class="site-footer">
  <h2 class="abs display">Tovesca Group</h2>
  <p class="abs">We are an innovative team of geospatial experts with 25 years of experience in the field of GIS. We specialize in providing results-driven GIS solutions for local government and the private sector.</p>
  <div class="abs social" aria-label="Social links"><span></span><span></span><span></span><span></span></div>
  <div class="abs rule"></div>
  <div class="abs copyright">© Copyright 2024 Tovesca Group | All Right Reserveds</div>
  <div class="abs to-top"><svg width="16" height="16"><path d="M3 11l5-5 5 5" stroke="#fff" stroke-width="2" fill="none"/></svg></div>
</footer>

</body>
</html>
```